Need a plumber

Would like a postcard sized flyer made up. Want the design to be kept very simple.
List of services we carry out in bullet point or similar.
Phone number and email included on the flyer.
Logo to feature prominantly.

List of services: Hot water issues
Burst Pipes
Gas Plumbing
Roof leaks
Drain blockages

Target Market(s)

Mums, dads and hosehgold owners

Industry/Entity Type

Plumbing

Colors
0054AA
0677BA
7BADD7
CADEEF
E8F1F8

Requirements
Must have
• Services we off and our logo, also must say "local plumber"

```html
<!DOCTYPE html>
<html lang="en">
<head>
<meta charset="utf-8">
<title>Clearflow Plumbing Co – Flyer</title>
<link href="https://fonts.googleapis.com/css2?family=Bebas+Neue&family=Montserrat:ital,wght@0,600;0,700;0,800;1,800&display=swap" rel="stylesheet">
<style>
  :root {
    --backdrop: #e6e7e8;
    --paper: #ffffff;
    --ink: #111111;
    --brand-blue: #2c62b0;
    --accent-blue: #3a9ad9;
    --ring-blue: #0677ba;
    --pale-blue: #cadeef;
    --mist-blue: #e8f1f8;
    --tab-black: #0d0d0d;
  }
  * { margin: 0; padding: 0; box-sizing: border-box; }
  html, body {
    width: 875px; height: 1200px; overflow: hidden;
    background: var(--backdrop);
  }
  .flyer {
    position: absolute; left: 99px; top: 92px;
    width: 678px; height: 1016px;
    background: var(--paper);
    overflow: hidden;
    font-family: "Montserrat", Arial, sans-serif;
    color: var(--ink);
  }
  .brand-tab {
    position: absolute; left: 21px; top: 0;
    width: 215px; height: 256px;
    background: var(--tab-black);
    border-radius: 0 0 90px 90px;
    display: flex; flex-direction: column; align-items: center; justify-content: center;
    gap: 12px;
  }
  .brand-dot {
    width: 34px; height: 34px; border-radius: 50%;
    background: var(--accent-blue);
  }
  .brand-name {
    color: var(--paper);
    font-weight: 700; font-size: 21px; letter-spacing: 1px;
    text-align: center; line-height: 1.25;
  }
  .brand-tagline {
    color: var(--accent-blue);
    font-weight: 700; font-size: 12px; letter-spacing: 2px;
    text-align: center;
  }
  .hero-art { position: absolute; left: 0; top: 0; }
  .headline-lead {
    position: absolute; left: 26px; top: 278px;
    font-weight: 800; font-size: 79px; line-height: 1; letter-spacing: 1px;
  }
  .headline-main {
    position: absolute; left: 28px; top: 356px;
    font-family: "Bebas Neue", Impact, sans-serif;
    font-size: 199px; line-height: 1; color: var(--brand-blue);
    letter-spacing: 1px;
  }
  .services-title {
    position: absolute; left: 28px; top: 540px;
    font-weight: 800; font-style: italic; font-size: 34px; line-height: 1;
  }
  .service-list {
    position: absolute; left: 28px; top: 588px;
    list-style: none;
  }
  .service-list li {
    display: flex; align-items: center; gap: 12px;
    height: 45px;
    font-weight: 600; font-size: 28px;
  }
  .service-list svg { flex: none; }
  .call-box {
    position: absolute; left: 27px; top: 842px;
    width: 196px; height: 200px;
    border-top: 2px solid var(--ink);
    border-left: 2px solid var(--ink);
    border-top-left-radius: 22px;
  }
  .call-label {
    position: absolute; left: 43px; top: 852px;
    font-weight: 700; font-size: 30px; line-height: 1;
  }
  .call-phone {
    position: absolute; left: 42px; top: 886px;
    font-family: "Bebas Neue", Impact, sans-serif;
    font-size: 82px; line-height: 1; color: var(--brand-blue);
    letter-spacing: 1px; white-space: nowrap;
  }
  .call-email {
    position: absolute; left: 43px; top: 963px;
    font-weight: 600; font-size: 18px;
  }
  .plumber-photo {
    position: absolute; left: 448px; top: 542px;
    width: 202px; height: 474px;
    border-radius: 100px 100px 0 0;
    background: linear-gradient(180deg, #3b63b8 0%, #2a4f9e 55%, #c69a55 78%, #2a4f9e 100%);
  }
</style>
</head>
<body>
  <main class="flyer">
    <svg class="hero-art" width="678" height="400" viewBox="0 0 678 400">
      <defs>
        <linearGradient id="workshopTone" x1="0" y1="0" x2="1" y2="1">
          <stop offset="0" stop-color="#eef2f6"/>
          <stop offset="0.5" stop-color="#b9c6d3"/>
          <stop offset="1" stop-color="#8a5a3c"/>
        </linearGradient>
        <linearGradient id="bathroomTone" x1="0" y1="0" x2="1" y2="1">
          <stop offset="0" stop-color="#d9dde1"/>
          <stop offset="1" stop-color="#8d9298"/>
        </linearGradient>
      </defs>
      <path role="img" aria-label="Photo of a plumber fixing pipes under a sink"
            d="M264,0 L678,0 L678,372 C560,330 420,240 340,120 C305,70 282,35 264,0 Z"
            fill="url(#workshopTone)"/>
      <path d="M264,0 C282,35 305,70 340,120 C420,240 560,330 678,372"
            fill="none" stroke="var(--accent-blue)" stroke-width="3"/>
      <circle cx="522" cy="250" r="86" fill="var(--ring-blue)"/>
      <circle role="img" aria-label="Photo of a modern bathroom" cx="522" cy="250" r="76" fill="url(#bathroomTone)"/>
    </svg>

    <div class="brand-tab">
      <span class="brand-dot"></span>
      <span class="brand-name">CLEARFLOW<br>PLUMBING CO</span>
      <span class="brand-tagline">LOCAL PLUMBER</span>
    </div>

    <h1 class="headline-lead">NEED A</h1>
    <div class="headline-main">PLUMBER</div>

    <h2 class="services-title">SERVICES</h2>
    <ul class="service-list">
      <li><svg width="22" height="22" viewBox="0 0 22 22"><polygon points="11,1 20,6 20,16 11,21 2,16 2,6" fill="none" stroke="var(--accent-blue)" stroke-width="4"/></svg>Hot Water Issues</li>
      <li><svg width="22" height="22" viewBox="0 0 22 22"><polygon points="11,1 20,6 20,16 11,21 2,16 2,6" fill="none" stroke="var(--accent-blue)" stroke-width="4"/></svg>Burst Pipes</li>
      <li><svg width="22" height="22" viewBox="0 0 22 22"><polygon points="11,1 20,6 20,16 11,21 2,16 2,6" fill="none" stroke="var(--accent-blue)" stroke-width="4"/></svg>Gas Plumbing</li>
      <li><svg width="22" height="22" viewBox="0 0 22 22"><polygon points="11,1 20,6 20,16 11,21 2,16 2,6" fill="none" stroke="var(--accent-blue)" stroke-width="4"/></svg>Roof Leaks</li>
      <li><svg width="22" height="22" viewBox="0 0 22 22"><polygon points="11,1 20,6 20,16 11,21 2,16 2,6" fill="none" stroke="var(--accent-blue)" stroke-width="4"/></svg>Drain Blockages</li>
    </ul>

    <div class="plumber-photo" role="img" aria-label="Photo of a plumber in blue overalls and tool belt pointing at the services list"></div>

    <div class="call-box"></div>
    <div class="call-label">CALL NOW</div>
    <div class="call-phone">0400 123 987</div>
    <div class="call-email">hello@clearflowplumbing.com.au</div>
  </main>
</body>
</html>
```